Professional DJ Business Card

Business card for giving out to clubs and venues or interested groups that are in need of a professional DJ. I want something artistic and catchy/alluring, with a minimalist approach that gets just the vital amount of info and leaves the rest for inquiry via contacting me. Ideally I would like one side to have an image of something cool like an eye and my name, then the other side be the contact info, I am definitely feeling a black or dark colored card, but I am open to other designs. I am uploading a picture that I made that reflects a little of what I am *kind of* looking for.

Industry/Entity Type

Business

Contact Information for Business Card

Tomas Halvik (Voxtel)
Professional DJ (West Coast)
EDM (Deep/House/Techno), Hip Hop, Latin, Trap.
Cell: 555-274-9163
Email: Voxtelofficial@mailnest.net
www.beatcloudia.net/yourtuneisfading

```html
<!DOCTYPE html>
<html lang="en">
<head>
<meta charset="utf-8">
<title>Tomas Halvik – DJ Business Card</title>
<link rel="stylesheet" href="https://fonts.googleapis.com/css2?family=Arimo:wght@400;700&family=Kaushan+Script&display=swap">
<style>
  :root {
    --backdrop: #e6e3de;
    --card-dark: #0d0d0d;
    --card-light: #ffffff;
    --ink: #111111;
    --paper: #ffffff;
    --record-mid: #2a2a2a;
    --shadow: rgba(0, 0, 0, 0.18);
  }
  * { margin: 0; padding: 0; box-sizing: border-box; }
  html, body {
    width: 1200px;
    height: 842px;
    overflow: hidden;
    background: var(--backdrop);
  }
  .sheet {
    width: 1200px;
    height: 842px;
    display: flex;
    flex-direction: column;
    align-items: center;
    justify-content: center;
    gap: 40px;
  }
  .card {
    position: relative;
    width: 620px;
    height: 354px;
    box-shadow: 0 6px 18px var(--shadow);
    overflow: hidden;
  }

  /* Front: dark side with the DJ name */
  .card--front {
    background: var(--card-dark);
    display: flex;
    align-items: center;
    justify-content: center;
    flex-direction: column;
  }
  .front-emblem {
    width: 260px;
    height: 120px;
    margin-bottom: 6px;
    border-radius: 60px / 40px;
    background: radial-gradient(ellipse at center, #6b6b6b 0%, #262626 55%, var(--card-dark) 80%);
  }
  .front-name {
    display: flex;
    align-items: center;
    gap: 14px;
  }
  .front-name__dot {
    width: 14px;
    height: 14px;
    border-radius: 50%;
    background: var(--paper);
  }
  .front-name__text {
    font-family: "Kaushan Script", cursive;
    font-size: 64px;
    color: var(--paper);
    line-height: 1.1;
  }

  /* Back: light side with contact details */
  .card--back {
    background: var(--card-light);
    color: var(--ink);
  }
  .identity {
    position: absolute;
    left: 92px;
    top: 42px;
    font-family: "Kaushan Script", cursive;
    font-weight: 400;
    color: var(--ink);
  }
  .identity__first,
  .identity__last {
    display: block;
    font-size: 54px;
    line-height: 1;
  }
  .identity__last { margin-left: 10px; }
  .identity__alias {
    display: block;
    font-size: 18px;
    text-align: right;
    margin-top: 2px;
  }
  .contact {
    position: absolute;
    right: 282px;
    top: 196px;
    font-family: "Arimo", sans-serif;
    font-size: 12.5px;
    line-height: 1.35;
    text-align: right;
    list-style: none;
  }
  .contact__label { font-weight: 700; }
  .contact__line--pad { margin-top: 8px; }
  .record-art {
    position: absolute;
    right: 38px;
    top: 46px;
    width: 236px;
    height: 236px;
    border-radius: 50%;
    background: radial-gradient(circle at center, #d9d9d9 0%, var(--record-mid) 45%, var(--card-dark) 70%);
  }
</style>
</head>
<body>
<main class="sheet">

  <section class="card card--front" aria-label="Card front">
    <div class="front-emblem" role="img" aria-label="Stylised eye illustration"></div>
    <div class="front-name">
      <span class="front-name__dot"></span>
      <span class="front-name__text">Voxtel</span>
    </div>
  </section>

  <section class="card card--back" aria-label="Card back">
    <h1 class="identity">
      <span class="identity__first">Tomas</span>
      <span class="identity__last">Halvik</span>
      <span class="identity__alias">(Voxtel)</span>
    </h1>

    <ul class="contact">
      <li>Professional DJ (West Coast)</li>
      <li>EDM (Deep/House/Techno), Hip Hop, Latin, Trap</li>
      <li><span class="contact__label">C:</span> 555-274-9163</li>
      <li class="contact__line--pad"><span class="contact__label">E:</span> Voxtelofficial@mailnest.net</li>
      <li class="contact__line--pad"><span class="contact__label">W:</span> www.beatcloudia.net/yourtuneisfading</li>
    </ul>

    <div class="record-art" role="img" aria-label="Vinyl record illustration"></div>
  </section>

</main>
</body>
</html>
```